Joy Under The Canopy poster

I would like to have a poster designed for my business. My website is www.joyunderthecanopy-example.com. This will give you an idea of what I do. If you need any images, let me know. I would like the phrase " Personalize your home away from home" used in the design...Thank you !
Updates

I'm not sure if you have received the pics I've uploaded...I have more to upload also...Thanks !

I've uploaded some photos...Send me some designs...lol

Target Market(s)

I will be displaying these posters in RV dealerships. I want the customer to see my new product so include pics.

Industry/Entity Type

Business

Requirements
Must have
• Include my website address but don't make it the focal point...I want the customers to order from the dealerships but if they want to see the options, they can go to the website.
Nice to have
• When you use my logo, please do not use the white block around it...

```html
<!DOCTYPE html>
<html lang="en">
<head>
<meta charset="utf-8">
<title>Joy Under The Canopy – Poster</title>
<link href="https://fonts.googleapis.com/css2?family=Delius&display=swap" rel="stylesheet">
<style>
  :root {
    --sky-deep: #86c6e2;
    --sky-mid: #a9d8ec;
    --band-light: #eaf6fb;
    --band-edge: #c4e4f2;
    --brand-blue: #1a2fe0;
    --brand-red: #e8102a;
    --ink: #0a0a0a;
    --photo-frame: #5f6b73;
  }
  html, body { margin: 0; padding: 0; overflow: hidden; }
  body { width: 943px; height: 1200px; }
  .poster {
    position: relative;
    width: 943px;
    height: 1200px;
    overflow: hidden;
    background: linear-gradient(180deg, var(--sky-mid) 0%, var(--sky-deep) 100%);
    font-family: "Delius", "Comic Sans MS", cursive;
  }
  .wave-band { position: absolute; inset: 0; }
  .brand {
    position: absolute;
    left: 0; right: 0; top: 34px;
    text-align: center;
  }
  .brand-name {
    margin: 0;
    font-size: 64px;
    font-weight: 400;
    color: var(--brand-blue);
    letter-spacing: 1px;
    line-height: 1.1;
  }
  .brand-tagline {
    margin: 14px 0 0;
    font-size: 38px;
    color: var(--brand-red);
    line-height: 1.1;
  }
  .headline {
    position: absolute;
    left: 0; right: 0; top: 415px;
    margin: 0;
    text-align: center;
    font-size: 82px;
    font-weight: 400;
    line-height: 1.45;
    color: var(--ink);
    text-shadow: 2px 3px 3px rgba(0,0,0,0.25);
  }
  .photo {
    position: absolute;
    box-shadow: 2px 3px 5px rgba(0,0,0,0.35);
  }
  .photo-trailer {
    left: 587px; top: 776px; width: 356px; height: 218px;
    background: linear-gradient(180deg, #b9d6ee 0%, #2c5fb8 45%, #d28a2e 70%, #5c564e 100%);
  }
  .photo-motorhome {
    left: 10px; top: 981px; width: 317px; height: 202px;
    background: linear-gradient(180deg, #6f7a5a 0%, #e9ecef 35%, #cfd3d6 70%, #4f5a3e 100%);
  }
  .website {
    position: absolute;
    right: 16px; top: 1086px;
    margin: 0;
    font-size: 29px;
    color: var(--ink);
  }
</style>
</head>
<body>
  <main class="poster">
    <svg class="wave-band" width="943" height="1200" viewBox="0 0 943 1200" aria-hidden="true">
      <defs>
        <linearGradient id="bandFill" x1="0" y1="0" x2="0" y2="1">
          <stop offset="0" stop-color="var(--band-edge)"/>
          <stop offset="0.45" stop-color="var(--band-light)"/>
          <stop offset="1" stop-color="#ffffff"/>
        </linearGradient>
      </defs>
      <path d="M0 372 C150 360 240 240 470 290 C640 325 760 310 943 290
               L943 700 C800 705 660 760 520 805 C340 862 180 845 0 770 Z"
            fill="url(#bandFill)"/>
    </svg>

    <header class="brand">
      <h1 class="brand-name">Joy Under The Canopy</h1>
      <p class="brand-tagline">Custom RV Awnings</p>
    </header>

    <h2 class="headline">Personalize your home<br>away from home</h2>

    <div class="photo photo-trailer" role="img" aria-label="Photo of an event trailer with a custom printed blue and orange awning extended"></div>
    <div class="photo photo-motorhome" role="img" aria-label="Photo of a white motorhome with a custom printed team mascot awning extended"></div>

    <p class="website">www.joyunderthecanopy-example.com</p>
  </main>
</body>
</html>
```